National Intensive Course Provider needs an advert designed to appear in trams

We need an advertisement designed to put in trams, the dimensions are 660mm wide and 203mm height. We offer intensive driving courses all over the UK, allowing pupils to complete a full driving course within a week/two weeks with both the theory and practical tests included in the course (as required). We would like the colours used to be green and dark blue, maybe red also, whatever looks best from them colours really.

Key Points to highlight:
- Pass your driving test within 1 week
- Start your course as early as next week
- Both tests included as part of your course (if required)

I have attached some images which could be included in the design

```html
<!DOCTYPE html>
<html lang="en">
<head>
<meta charset="UTF-8">
<title>Intensive Driving Course – Tram Advert</title>
<link href="https://fonts.googleapis.com/css2?family=Tinos&family=Archivo:wght@700&display=swap" rel="stylesheet">
<style>
  :root {
    --navy: #15238a;
    --panel: #2a3a9c;
    --amber: #e9a20c;
    --white: #ffffff;
    --shadow: #000000;
    --tick: #e0131b;
    --box: #1a1a3a;
    --photo-light: #c9ccd2;
    --photo-mid: #7d8aa8;
    --photo-dark: #3b4666;
  }
  html, body {
    margin: 0;
    padding: 0;
    overflow: hidden;
    background: var(--white);
  }
  .advert {
    position: relative;
    width: 1200px;
    height: 369px;
    overflow: hidden;
    background: var(--navy);
  }
  .advert svg { position: absolute; inset: 0; }
  .serif { font-family: "Tinos", "Times New Roman", serif; }
  .sans { font-family: "Archivo", "Arial", sans-serif; font-weight: 700; }
  .brand-name {
    font-family: "Tinos", "Times New Roman", serif;
    font-size: 13px;
    fill: var(--white);
  }
  .strapline { font-size: 21px; fill: var(--white); }
  .headline-serif { font-size: 104px; fill: var(--white); }
  .headline-sans { font-size: 64px; fill: var(--white); }
  .headline-shadow { fill: var(--shadow); }
  .benefit { font-size: 21px; fill: var(--white); }
</style>
</head>
<body>
<div class="advert">
  <svg width="1200" height="369" viewBox="0 0 1200 369" xmlns="http://www.w3.org/2000/svg">
    <defs>
      <linearGradient id="photo-tones" x1="0" y1="0" x2="1" y2="1">
        <stop offset="0" stop-color="var(--photo-dark)"/>
        <stop offset="0.5" stop-color="var(--photo-mid)"/>
        <stop offset="1" stop-color="var(--photo-light)"/>
      </linearGradient>
    </defs>

    <!-- text panel -->
    <rect class="text-panel" x="26" y="35" width="700" height="297" fill="var(--panel)"/>

    <!-- diagonal bands -->
    <polygon class="band-amber" points="506,369 938,0 972,0 604,369" fill="var(--amber)"/>
    <polygon class="band-white" points="604,369 972,0 990,0 656,369" fill="var(--white)"/>

    <!-- photo area -->
    <polygon class="photo-area" points="656,369 990,0 1200,0 1200,369" fill="url(#photo-tones)"
             role="img" aria-label="Photo of a smiling driver leaning out of a car window giving a thumbs up"/>

    <!-- brand -->
    <rect x="8" y="14" width="72" height="52" rx="8" fill="var(--navy)" stroke="var(--white)" stroke-width="0"/>
    <text class="brand-name" x="44" y="37" text-anchor="middle">Northway</text>
    <text class="brand-name" x="44" y="53" text-anchor="middle">Driving</text>

    <!-- headline -->
    <text class="serif strapline" x="253" y="58" textLength="425" lengthAdjust="spacing">ALL OVER THE UK</text>

    <text class="serif headline-serif headline-shadow" x="99" y="148" textLength="492" lengthAdjust="spacingAndGlyphs">INTENSIVE</text>
    <text class="serif headline-serif" x="96" y="145" textLength="492" lengthAdjust="spacingAndGlyphs">INTENSIVE</text>

    <text class="sans headline-sans headline-shadow" x="302" y="210" textLength="468" lengthAdjust="spacingAndGlyphs">DRIVING  COURSE</text>
    <text class="sans headline-sans" x="299" y="207" textLength="468" lengthAdjust="spacingAndGlyphs">DRIVING  COURSE</text>

    <!-- benefits -->
    <g class="benefit-item">
      <rect x="28" y="237" width="17" height="17" fill="var(--box)" stroke="var(--tick)" stroke-width="2"/>
      <path d="M31 243 L38 252 L58 220" fill="none" stroke="var(--tick)" stroke-width="4" stroke-linecap="round" stroke-linejoin="round"/>
      <text class="serif benefit" x="56" y="257">Pass your</text>
      <text class="serif benefit" x="56" y="285">driving test</text>
      <text class="serif benefit" x="56" y="312">within 1 week</text>
    </g>
    <g class="benefit-item">
      <rect x="254" y="237" width="17" height="17" fill="var(--box)" stroke="var(--tick)" stroke-width="2"/>
      <path d="M257 243 L264 252 L284 220" fill="none" stroke="var(--tick)" stroke-width="4" stroke-linecap="round" stroke-linejoin="round"/>
      <text class="serif benefit" x="284" y="257">Start your</text>
      <text class="serif benefit" x="284" y="285">course as early</text>
      <text class="serif benefit" x="284" y="312">as next week</text>
    </g>
    <g class="benefit-item">
      <rect x="481" y="237" width="17" height="17" fill="var(--box)" stroke="var(--tick)" stroke-width="2"/>
      <path d="M484 243 L491 252 L511 220" fill="none" stroke="var(--tick)" stroke-width="4" stroke-linecap="round" stroke-linejoin="round"/>
      <text class="serif benefit" x="509" y="257">Both tests</text>
      <text class="serif benefit" x="509" y="285">included as part</text>
      <text class="serif benefit" x="509" y="312">of your course</text>
      <text class="serif benefit" x="509" y="340">(if required)</text>
    </g>
  </svg>
</div>
</body>
</html>
```